"You CAN Relax on Your Own Savings!" book cover for 80 page or so book.

Need a book cover that stands out on Bookvale, so highly engaging colors, need to reflect optimism, hope and determination. Go to Bookvale, type my name in and see the covers for the three other books I had written.

There's a lot of negativity and fear for Americans looking at retirement. Yet, they don't need that fear, my book tells them why they can be confident in their ability to retire.

There will be NO spine writing for the book, too small.

Target Market(s)

stressed out people in their 50s and 60s. This book appeals to working people, not high end, wealthy types.

Industry/Entity Type

Financial Planning

Colors

Designer to choose colors to be used in the design.

Requirements
Must have
• Needs to reflect simplicity in action.
• Please spell out my full name, GREG MALTHORPE, at the bottom of the cover.
Nice to have
• if there is anyway to put a picture of an RV (Recreational Vehicle) that would be great.
Should not have
• Do NOT want to be the stodgy, typical financial planning literature out there. No guy in a suit and tie. No one sitting on a beach.
• Do not want my face on the cover either. (On the back yes.)

```html
<!DOCTYPE html>
<html lang="en">
<head>
<meta charset="utf-8">
<title>You CAN Relax on Your Own Savings! — Book Cover</title>
<link rel="stylesheet" href="https://fonts.googleapis.com/css2?family=Libre+Caslon+Text:ital,wght@0,400;1,400&display=swap">
<style>
  :root {
    --page-bg: #ffffff;
    --cover-pink: #f9a4a1;
    --sky-rose: #f6a2a4;
    --sky-lilac: #e7a3b2;
    --horizon-mauve: #c7a1b1;
    --rv-cream: rgba(238, 226, 212, 0.85);
    --window-glow: rgba(214, 120, 40, 0.55);
    --scrub-olive: #6d6a3c;
    --scrub-dark: #3a3b1f;
    --ink-dark: #231f20;
    --ink-light: #ffffff;
    --cover-edge: #5a3a38;
  }
  * { margin: 0; padding: 0; box-sizing: border-box; }
  html, body {
    width: 1200px;
    height: 1200px;
    overflow: hidden;
    background: var(--page-bg);
  }
  .canvas {
    position: relative;
    width: 1200px;
    height: 1200px;
  }
  .cover {
    position: absolute;
    left: 410px;
    top: 299px;
    width: 375px;
    height: 561px;
    background: var(--cover-pink);
    border: 1px solid var(--cover-edge);
    overflow: hidden;
    font-family: "Libre Caslon Text", "Georgia", serif;
  }
  .cover-scene {
    position: absolute;
    left: 0;
    right: 0;
    top: 250px;
    bottom: 0;
    background:
      radial-gradient(ellipse 34% 9% at 62% 63%, var(--window-glow) 0%, rgba(214,120,40,0) 100%),
      radial-gradient(ellipse 48% 16% at 60% 61%, var(--rv-cream) 0%, rgba(238,226,212,0) 100%),
      linear-gradient(
        to bottom,
        rgba(249, 164, 161, 0) 0%,
        var(--sky-rose) 22%,
        var(--sky-lilac) 40%,
        var(--horizon-mauve) 50%,
        #a39a86 56%,
        var(--scrub-olive) 74%,
        var(--scrub-dark) 100%
      );
  }
  .book-title {
    font-weight: 400;
    font-size: inherit;
  }
  .title-line {
    position: absolute;
    left: 0;
    right: 0;
    text-align: center;
    white-space: nowrap;
    line-height: 1;
    font-weight: 400;
  }
  .title-main { font-size: 64px; color: var(--ink-dark); letter-spacing: -0.01em; }
  .title-accent { color: var(--ink-light); }
  .title-line--first { top: 12px; padding-left: 6px; }
  .title-line--second { top: 70px; color: var(--ink-light); }
  .title-line--connector {
    top: 138px;
    font-size: 24px;
    font-style: italic;
    color: var(--ink-dark);
  }
  .title-line--third { top: 157px; }
  .title-line--fourth { top: 213px; }
  .author {
    position: absolute;
    left: 0;
    right: 0;
    top: 293px;
    text-align: center;
    color: var(--ink-light);
    font-size: 25px;
    line-height: 32px;
    font-weight: 400;
  }
</style>
</head>
<body>
  <div class="canvas">
    <div class="cover">
      <div class="cover-scene" role="img" aria-label="Desert at dusk with saguaro cacti, scrub brush and a white RV with warmly lit windows under a pink sky"></div>

      <h1 class="book-title">
        <span class="title-line title-line--first title-main">You <span class="title-accent">CAN</span></span>
        <span class="title-line title-line--second title-main title-accent">Relax</span>
        <span class="title-line title-line--connector">ON YOUR</span>
        <span class="title-line title-line--third title-main">Own</span>
        <span class="title-line title-line--fourth title-main">Savings!</span>
      </h1>

      <p class="author">GREG<br>MALTHORPE</p>
    </div>
  </div>
</body>
</html>
```